LVNODE
biz card
LVNODE - Information Technology
Creative Brief
Professional
jun pa
238 Elmora Pl, 3FL NewYorkCity, NY 10583
jun.pa@lanviretnode.com
www.lanviretnode.com

```html
<!DOCTYPE html>
<html lang="en">
<head>
<meta charset="utf-8">
<title>LVNODE Stationery Set</title>
<link href="https://fonts.googleapis.com/css2?family=Montserrat:wght@400;600;700&display=swap" rel="stylesheet">
<style>
:root{
  --stage:#a7a8aa;
  --paper:#ffffff;
  --brand-red:#d7282f;
  --brand-dark:#8e1217;
  --ink:#4a4a4a;
  --shadow:rgba(0,0,0,.25);
}
*{box-sizing:border-box;margin:0;padding:0}
html,body{width:1200px;height:684px;overflow:hidden}
body{background:var(--stage);font-family:"Montserrat",Arial,sans-serif;position:relative;color:var(--ink)}
.sheet{position:absolute;background:var(--paper);box-shadow:1px 2px 4px var(--shadow);overflow:hidden}
.brand{display:flex;align-items:center;gap:6px;color:var(--brand-red);font-weight:700;letter-spacing:.5px;white-space:nowrap}
.brand-square{background:var(--brand-red);display:block}
.contact{position:absolute;list-style:none;font-size:6px;line-height:9px;color:var(--ink);white-space:nowrap}
.contact li{display:flex;align-items:center;gap:4px}
.dot{width:4px;height:4px;border-radius:50%;background:var(--brand-red);flex:none}
.band{position:absolute;left:0;right:0;bottom:0;background:linear-gradient(var(--brand-red),var(--brand-dark))}
.band-text{position:absolute;left:12px;bottom:4px;font-size:6px;color:#fff;white-space:nowrap}

/* business card */
.card{left:12px;top:283px;width:168px;height:96px;z-index:2}
.card .brand{position:absolute;left:8px;top:8px;font-size:11px}
.card .brand-square{width:15px;height:15px}
.card .contact{left:8px;top:48px;font-size:5px;line-height:7.5px}
.card .contact .dot{width:3px;height:3px}
.card .band{height:11px}
.card .band-text{left:8px;bottom:3px;font-size:5px}
.card .holder{position:absolute;right:8px;bottom:15px;font-size:6px;font-weight:600;color:var(--brand-red);white-space:nowrap}

/* letterhead */
.letterhead{left:190px;top:19px;width:368px;height:643px}
.letterhead .brand{position:absolute;left:20px;top:28px;flex-direction:column;align-items:flex-start;gap:8px;font-size:15px}
.letterhead .brand-square{width:34px;height:34px}
.letterhead .contact{left:24px;top:584px}
.letterhead .band{height:22px}

/* envelope back */
.envelope{left:643px;top:96px;width:545px;height:228px}
.envelope svg.flap{position:absolute;left:0;top:0}
.envelope .brand{position:absolute;left:248px;top:60px;font-size:12px}
.envelope .brand-square{width:18px;height:18px}

/* compliment slip */
.slip{left:643px;top:379px;width:545px;height:283px}
.slip .brand{position:absolute;left:14px;top:20px;flex-direction:column;align-items:flex-start;gap:6px;font-size:14px}
.slip .brand-square{width:28px;height:28px}
.slip .contact{left:22px;top:152px}
.slip .band{height:24px;background:var(--brand-dark)}
.slip .band::before{content:"";position:absolute;left:0;right:0;top:0;height:14px;background:var(--brand-red)}
.slip .band-text{bottom:12px;z-index:1}
</style>
</head>
<body>

<section class="sheet card" aria-label="Business card">
  <div class="brand"><span class="brand-square"></span>LVNODE</div>
  <ul class="contact">
    <li><span class="dot"></span>T: 212 555 0147</li>
    <li><span class="dot"></span>F: 212 555 0148</li>
    <li><span class="dot"></span>jun.pa@lanviretnode.com</li>
    <li><span class="dot"></span>238 Elmora Pl, 3FL NewYorkCity, NY 10583</li>
  </ul>
  <p class="holder">jun pa</p>
  <div class="band"><span class="band-text">www.lanviretnode.com</span></div>
</section>

<section class="sheet letterhead" aria-label="Letterhead">
  <div class="brand"><span class="brand-square"></span>LVNODE</div>
  <ul class="contact">
    <li><span class="dot"></span>T: 212 555 0147</li>
    <li><span class="dot"></span>F: 212 555 0148</li>
    <li><span class="dot"></span>jun.pa@lanviretnode.com</li>
    <li><span class="dot"></span>238 Elmora Pl, 3FL NewYorkCity, NY 10583</li>
  </ul>
  <div class="band"><span class="band-text">www.lanviretnode.com</span></div>
</section>

<section class="sheet envelope" aria-label="Envelope back">
  <svg class="flap" width="545" height="228" viewBox="0 0 545 228">
    <path d="M0 2 C120 30 200 70 272 72 C344 70 425 30 545 2" fill="none" stroke="#c9c9c9" stroke-width="1.2"/>
  </svg>
  <div class="brand"><span class="brand-square"></span>LVNODE</div>
</section>

<section class="sheet slip" aria-label="Compliment slip">
  <div class="brand"><span class="brand-square"></span>LVNODE</div>
  <ul class="contact">
    <li><span class="dot"></span>T: 212 555 0147</li>
    <li><span class="dot"></span>F: 212 555 0148</li>
    <li><span class="dot"></span>jun.pa@lanviretnode.com</li>
    <li><span class="dot"></span>238 Elmora Pl, 3FL NewYorkCity, NY 10583</li>
  </ul>
  <div class="band"><span class="band-text">www.lanviretnode.com</span></div>
</section>

</body>
</html>
```